Larkspur Homes - wanted BRILLIANT website design for our new property investing company

We need a website design for our new company based in Bristol, England, UK called "Larkspur Homes". We help buy people property who are in financial difficulty or who are needing to sell their property quickly for reasons such as death, divorce/separation, relocation, emigration.

We have a logo being designed incorporating strawberry and property (so red and green). We would like designs to communicate an elegant ,professional, approachable, friendly
fresh clean but also warm appealing appearance
Not too busy
Website consistent with logo and company name i.e. colour scheme

Please use our word document for content as a guide but use professional judgement for minor alterations if you feel they would benefit the site/structure etc

Please ask at any time if not sure

Target Market(s)

Adult british population, those that have a mortgage / loan / own property

Industry/Entity Type

Financial

Font styles to use
Serif
Sans Serif
Decorative

Colors
0692cd
33b7a4
acd036
fbee3e
3176b5
886aae
a6479a
e567a6
eb1f27

Requirements
Must have
• This must not look like a template website we are looking for UNIQUE please!
Nice to have
• Bristol pictures instead of generic, or colourful line drawings/comic drawings of houses/property/keys/happy people.....
Should not have
• An obvious off the shelf template design

```html
<!DOCTYPE html>
<html lang="en">
<head>
<meta charset="utf-8">
<title>Larkspur Homes</title>
<link rel="stylesheet" href="https://fonts.googleapis.com/css2?family=Open+Sans:wght@400;600;700&display=swap">
<style>
:root{
  --red:#d41200;
  --nav:#650b05;
  --nav-active:#7a0e06;
  --green:#3cb21a;
  --hero:#6f9f4a;
  --hero-deep:#5a8c38;
  --ink:#444;
  --muted:#7a7a7a;
  --panel:#eeeeee;
  --footer:#e4e4e4;
  --white:#fff;
}
*{box-sizing:border-box;margin:0;padding:0}
html,body{width:860px;height:1200px;overflow:hidden}
body{position:relative;background:var(--white);font-family:"Open Sans",Arial,sans-serif;color:var(--ink)}
.abs{position:absolute}
.top-band{left:0;top:0;width:860px;height:108px;background:var(--red)}
.brand{left:70px;top:31px;color:var(--white);font-size:17px;font-weight:600;letter-spacing:.2px}
.enquiry{left:503px;top:11px;display:flex;gap:6px;align-items:flex-start;color:var(--white)}
.enquiry small{display:block;font-size:9px;line-height:11px}
.enquiry strong{display:block;font-size:13px;line-height:14px;font-weight:700}
.email{left:633px;top:16px;color:var(--white);font-size:10.5px;font-weight:600}
.main-nav{left:71px;top:75px;width:719px;height:52px;background:var(--nav);display:flex;padding-left:29px}
.main-nav a{display:block;height:52px;line-height:52px;padding:0 15px;color:var(--white);font-size:10.5px;text-decoration:none;text-transform:uppercase}
.main-nav a.active{background:var(--nav-active);color:var(--green);border-bottom:2px solid var(--red)}
.main-nav a.wide{padding:0 16px}
.hero{left:71px;top:134px;width:719px;height:312px;background:linear-gradient(180deg,var(--hero) 0%,var(--hero-deep) 100%)}
.hero-dots{left:712px;top:155px;display:flex;gap:9px}
.hero-dots span{width:7px;height:7px;background:#e8eef3}
.hero-dots span.on{background:var(--green)}
.hero-caption{left:207px;top:387px;width:445px;height:59px;background:rgba(35,65,15,.78);color:var(--white);font-size:17px;line-height:59px;text-align:center}
.intro{left:71px;top:480px;font-size:10.5px;line-height:13px;color:#333}
.ticks{list-style:none}
.ticks li{position:relative;padding-left:22px;font-size:10.5px;height:24px;line-height:14px;color:var(--ink)}
.ticks li::before{content:"";position:absolute;left:0;top:1px;width:10px;height:10px;border:1.5px solid #777;border-radius:50%;background:radial-gradient(circle,#777 0 2px,transparent 2.5px)}
.services{left:71px;top:531px}
.help{left:417px;top:482px;width:372px;height:252px;background:var(--panel)}
.help h2{position:absolute;left:28px;top:19px;font-size:13px;font-weight:400;color:#444}
.help .col1{left:28px;top:49px}
.help .col2{left:207px;top:49px}
.help .ticks li{padding-left:18px}
.appointment{left:71px;top:766px;width:456px;height:243px;background:var(--panel)}
.appointment h2{position:absolute;left:26px;top:18px;font-size:18px;font-weight:400;color:#444}
.appointment p{position:absolute;left:26px;top:43px;width:290px;font-size:10.5px;line-height:12px;color:#555}
.field{position:absolute;background:var(--white);border:1px solid #dcdcdc;font-size:9.5px;color:#888;padding:6px 7px;height:25px}
.submit{left:362px;top:192px;width:65px;height:26px;background:var(--green);color:var(--white);font-size:10px;font-weight:700;text-align:center;line-height:26px}
.consult{left:546px;top:766px;width:243px;height:243px;background:var(--panel)}
.consult .photo{left:0;top:0;width:243px;height:160px;background:linear-gradient(180deg,#c9d9e6 0%,#e5edf3 60%,#eeeeee 100%)}
.consult h3{position:absolute;left:0;width:243px;top:154px;text-align:center;font-size:12.5px;font-weight:600;color:#444}
.consult p{position:absolute;left:0;width:243px;top:174px;text-align:center;font-size:10px;line-height:12px;color:#444}
.consult .cta{left:74px;top:215px;width:96px;height:28px;background:var(--green);color:var(--white);font-size:10px;line-height:28px;text-align:center}
.footer{left:0;top:1042px;width:860px;height:158px;background:var(--footer)}
.foot-col{position:absolute;top:26px}
.foot-col h4{font-size:12px;font-weight:600;color:var(--green);margin-bottom:3px}
.foot-col li{list-style:none;font-size:8px;line-height:10.5px;color:var(--muted);text-transform:uppercase}
.social{left:722px;top:1138px;display:flex;gap:4px}
.social span{width:20px;height:20px;border-radius:50%;background:#6f6f6f}
.copyright{left:440px;top:1173px;width:349px;text-align:right;font-size:8px;color:var(--muted);text-transform:uppercase}
</style>
</head>
<body>
<div class="abs top-band"></div>
<div class="abs brand">LARKSPUR HOMES</div>
<div class="abs enquiry">
  <svg width="14" height="24" viewBox="0 0 14 24"><rect x="1" y="1" width="12" height="22" rx="2" fill="#7a0e06"/><rect x="3" y="4" width="8" height="7" fill="#d41200"/><g fill="#d41200"><rect x="3" y="13" width="2" height="2"/><rect x="6" y="13" width="2" height="2"/><rect x="9" y="13" width="2" height="2"/><rect x="3" y="17" width="2" height="2"/><rect x="6" y="17" width="2" height="2"/><rect x="9" y="17" width="2" height="2"/></g></svg>
  <div><small>For enquiries call</small><strong>0770 0900 316</strong></div>
</div>
<div class="abs email">info@larkspur-homes.co.uk</div>

<nav class="abs main-nav">
  <a class="active">Home</a>
  <a>Sell your property fast</a>
  <a class="wide">Rent your property fast</a>
  <a>The 5 easy steps</a>
  <a>About us</a>
  <a>Contact</a>
</nav>

<div class="abs hero" role="img" aria-label="Photo of a country club house with trees and lawns under a blue sky"></div>
<div class="abs hero-dots"><span class="on"></span><span></span><span></span><span></span></div>
<div class="abs hero-caption">Do you want to sell or rent out your house quickly?</div>

<p class="abs intro">Do you want to sell or rent out your house quickly?<br>We are a local family run property business who specialize in;</p>
<ul class="abs ticks services">
  <li>Buying properties quickly</li>
  <li>Finding creative solutions to your property problems</li>
  <li>Property rental management</li>
  <li>Lettings to professional and student tenants</li>
  <li>Guaranteed rent and management schemes for landlords</li>
  <li>STOPPING repossessions</li>
  <li>Motivated sellers</li>
  <li>Chain fixing</li>
  <li>Negative equity problems</li>
</ul>

<section class="abs help">
  <h2>How can we help?</h2>
  <ul class="abs ticks col1">
    <li>How &nbsp;to stop repossession</li>
    <li>Divorce or separation</li>
    <li>Financial problems</li>
    <li>Don’t like estate agents?</li>
    <li>Property needing work</li>
    <li>Retiring landlords</li>
    <li>Negative equity</li>
    <li>Opportunity not to be missed!!</li>
  </ul>
  <ul class="abs ticks col2">
    <li>Guaranteed rent scheme</li>
    <li>Ill health</li>
    <li>Relocating</li>
    <li>Inherited property</li>
    <li>Chain Collapse</li>
    <li>Tenanted Property</li>
  </ul>
</section>

<section class="abs appointment">
  <h2>Make an Appointment</h2>
  <p>Like to make an enquiry? Here you can enter more details about your enquiry.</p>
  <div class="field" style="left:26px;top:81px;width:192px">Your name</div>
  <div class="field" style="left:236px;top:81px;width:192px">Property address</div>
  <div class="field" style="left:26px;top:121px;width:192px">Email address</div>
  <div class="field" style="left:236px;top:121px;width:192px;height:65px">Message</div>
  <div class="field" style="left:26px;top:161px;width:192px">Phone number</div>
  <div class="abs submit">SUBMIT</div>
</section>

<section class="abs consult">
  <div class="abs photo" role="img" aria-label="Photo of two people shaking hands"></div>
  <h3>Free Consultation</h3>
  <p>Let us find the right solution<br>for your Needs</p>
  <div class="abs cta">CLICK HERE &nbsp;<svg width="8" height="11" viewBox="0 0 8 11" style="vertical-align:-1px"><path d="M1.5 1l5 4.5-5 4.5" fill="none" stroke="#fff" stroke-width="2"/></svg></div>
</section>

<footer class="abs footer">
  <div class="foot-col" style="left:70px"><h4>MENU LINKS</h4><ul><li>Blog</li><li>About us</li><li>A-Z People</li><li>Help</li></ul></div>
  <div class="foot-col" style="left:188px"><h4>QUICK LINKS</h4><ul><li>Home</li><li>For sale</li><li>News &amp; Events</li><li>Contact us</li></ul></div>
  <div class="foot-col" style="left:307px"><h4>CONTACT US</h4><ul><li>18 Alder Rd.</li><li>Westbury BS9 4QT</li><li>0117 496 0582</li><li>9 Mill Lane, Redland</li></ul></div>
</footer>
<div class="abs social"><span></span><span></span><span></span></div>
<div class="abs copyright">2014 © Copyright larkspur-homes | All rights reserved</div>
</body>
</html>
```